de Lorvanche Jewelry & Co. needs a website design

We need a website design for a new company based in Minnesota called 'de Lorvanche Jewelry & Co.' My wife and I are both geologists who handcraft fine jewelry using nephrite-jade from a newly discovered glacial deposit in Minnesota that I independently discovered, researched, and extracted. The jade colors range from a beautiful black to dark green and are mostly set in yellow gold, though we also use silver, platinum, and white gold. We will also be using nephrite-jade, jadeite-jade's from other parts of the world, including other semi- precious and precious stones such as black onyx/ chalcedony's, rubies ,sapphire, and diamonds. The family name 'de Lorvanche' means of the ash tree in French, and I would this motif to be incorporated into the website design. I've attached the files for our company logo and would like to blend that theme and emblem into the design as well in an elegant fashion. I'm aiming for a black jade/ dark green and yellow gold look am primarily interested in a design optimized for online shoppers. Additionally, I want a section where visitors can read a brief summary of our research and discovery story as geologists. Currently, we will be selling pendant necklaces, bead necklaces, earrings, bead bracelets, and bracelets. The website should convey that we sell fine, handcrafted, and very unique jewelry.

```html
<!DOCTYPE html>
<html lang="en">
<head>
<meta charset="utf-8">
<title>de Lorvanche Jewelry &amp; Co.</title>
<link rel="stylesheet" href="https://fonts.googleapis.com/css2?family=Poppins:wght@400;500;600;700;800&display=swap">
<style>
:root{
  --gold:#b38a2c;
  --gold-light:#c9a33a;
  --ink:#111111;
  --charcoal:#2f2f2f;
  --cream:#fcf4ec;
  --text:#222222;
  --muted:#555555;
  --white:#ffffff;
}
*{box-sizing:border-box;margin:0;padding:0}
html,body{width:1200px;height:4392px;overflow:hidden}
body{font-family:"Poppins",sans-serif;color:var(--text);background:var(--white);position:relative}
.abs{position:absolute}
.btn{position:absolute;display:flex;align-items:center;justify-content:center;background:var(--gold);color:var(--white);font-weight:600;font-size:18px;border-radius:30px}
/* top bar */
.topbar{top:0;left:0;width:1200px;height:51px;background:var(--charcoal);color:#ddd;font-size:14px;padding:16px 0 0 120px}
.nav{top:51px;left:0;width:1200px;height:119px;background:var(--white)}
.nav a{position:absolute;top:52px;font-size:15px;color:var(--text);text-decoration:none;letter-spacing:.3px}
.logo{position:absolute;top:0;left:490px;width:240px;height:100px;display:flex;flex-direction:column;align-items:center;justify-content:flex-end}
.logo .mark{width:42px;height:42px;border:3px solid var(--gold);margin-bottom:8px;background:var(--white)}
.logo .name{font-size:20px;font-weight:500;color:var(--charcoal);letter-spacing:1px}
.nav-icons{position:absolute;top:50px;left:1025px;display:flex;gap:18px}
/* hero */
.hero{top:170px;left:0;width:1200px;height:578px;background:#2e2e2e}
.hero-photo{position:absolute;left:440px;top:0;width:760px;height:578px;background:radial-gradient(ellipse at 60% 55%,#c6552d 0%,#4c9a94 35%,#3b4a3c 65%,#2e2e2e 100%)}
.hero h1{position:absolute;left:78px;top:138px;font-size:62px;line-height:64px;font-weight:800;color:var(--white)}
.hero p{position:absolute;left:77px;top:285px;font-size:23px;line-height:33px;font-weight:600;color:var(--white)}
.dots{position:absolute;left:74px;top:522px;display:flex;gap:14px}
.dots span{width:10px;height:10px;border-radius:50%;background:#777}
.dots span:first-child{background:var(--gold)}
/* categories */
.sec-title{position:absolute;width:1200px;left:0;text-align:center;font-size:42px;font-weight:700}
.cat{position:absolute;top:895px;width:330px;height:297px;background:var(--cream);border-radius:6px;text-align:center}
.cat .ph{width:160px;height:180px;margin:0 auto;border-radius:4px}
.cat h3{font-size:24px;font-weight:700;margin-top:22px}
.cat span{display:block;color:var(--gold);font-size:16px;margin-top:10px}
.arrow{position:absolute}
/* products */
.band{top:1265px;left:0;width:1200px;height:377px;background:linear-gradient(90deg,#b58a2e,#c9a63c)}
.prod{position:absolute;top:1396px;width:241px;height:399px;background:var(--white);border-radius:4px;box-shadow:0 2px 10px rgba(0,0,0,.12);text-align:center}
.prod .ph{width:200px;height:210px;margin:20px auto 0;border-radius:4px}
.prod h4{font-size:20px;font-weight:600;margin-top:12px}
.prod p{font-size:14px;color:var(--muted);line-height:20px;margin-top:6px;padding:0 20px}
.price{position:absolute;left:32px;top:331px;width:160px;height:46px;background:var(--ink);border-radius:23px;color:var(--white);font-weight:700;font-size:21px;display:flex;align-items:center}
.price i{width:38px;height:38px;border-radius:50%;background:var(--white);margin:0 20px 0 4px;display:flex;align-items:center;justify-content:center}
/* promos */
.promo{position:absolute;top:1991px;width:512px;height:480px;border-radius:3px;color:var(--white);text-align:center}
/* about */
.about-img{top:2547px;left:0;width:587px;height:589px;background:linear-gradient(180deg,#e7a994 0%,#8c8aa0 45%,#5b6166 70%,#7d7c6c 100%)}
.about{top:2547px;left:587px;width:613px;height:589px;background:var(--ink);color:var(--white);padding:68px 60px 0 28px}
.about h2{font-size:44px;line-height:48px;font-weight:700}
.about p{font-size:16px;line-height:30.5px;margin-top:22px;color:#eee}
/* blog */
.blog{position:absolute;top:3279px;width:330px}
.blog .ph{height:213px;border-radius:3px}
.blog p{font-size:18px;line-height:30px;margin-top:20px;color:var(--text)}
.blog time{display:block;font-size:13px;font-weight:600;color:var(--gold);margin-top:12px}
/* email */
.email{top:3797px;left:0;width:1200px;height:189px;background:var(--ink);color:var(--white)}
.email h2{position:absolute;left:72px;top:42px;font-size:44px;font-weight:700}
.email p{position:absolute;left:72px;top:112px;font-size:18px}
.email .field{position:absolute;left:674px;top:66px;width:453px;height:58px;border:1.5px solid #ccc;border-radius:30px;font-size:14px;color:var(--gold);padding:19px 0 0 22px}
/* footer */
.foot-logo{top:4080px;left:72px;width:225px;text-align:center}
.foot-col{position:absolute;top:4052px}
.foot-col h5{font-size:21px;font-weight:700;margin-bottom:12px}
.foot-col li{list-style:none;font-size:15px;color:var(--muted);line-height:34px}
.contact li{display:flex;gap:14px;line-height:27px;margin-bottom:10px}
.copy{top:4317px;left:0;width:1200px;height:75px;border-top:1px solid #ddd}
</style>
</head>
<body>

<div class="abs topbar">Sed ut perspiciatis unde omnis iste natus.</div>

<header class="abs nav">
  <a style="left:128px">ABOUT US</a>
  <a style="left:256px">PRODUCTS</a>
  <a style="left:390px">SHOP</a>
  <div class="logo"><div class="mark"></div><div class="name">DE LORVANCHE</div></div>
  <a style="left:763px">REVIEWS</a>
  <a style="left:878px">CONTACT</a>
  <div class="nav-icons">
    <svg width="18" height="18" viewBox="0 0 18 18" fill="none" stroke="#b38a2c" stroke-width="2.4"><circle cx="7.5" cy="7.5" r="5"/><path d="M11.5 11.5l5 5"/></svg>
    <svg width="18" height="18" viewBox="0 0 18 18" fill="#b38a2c"><circle cx="9" cy="5" r="4.5"/><path d="M1 18c0-5 3.5-7.5 8-7.5s8 2.5 8 7.5z"/></svg>
    <svg width="20" height="18" viewBox="0 0 20 18" fill="none" stroke="#b38a2c" stroke-width="2.2"><path d="M1 7h18l-2 10H3z M6 7l4-6 4 6"/></svg>
  </div>
</header>

<section class="abs hero">
  <div class="hero-photo" role="img" aria-label="Close-up of a colourful gemstone bead bracelet resting on a carved wooden bowl"></div>
  <h1>de Lorvanche<br>Jewelry &amp; Co</h1>
  <p>Sed ut perspiciatis unde omnis iste natus<br>error sit voluptatem</p>
  <div class="btn" style="left:82px;top:376px;width:199px;height:54px">Show Now</div>
  <div class="dots"><span></span><span></span><span></span><span></span></div>
</section>

<h2 class="sec-title" style="top:802px">Featured Categories</h2>
<svg class="arrow" style="left:40px;top:1028px" width="20" height="32" viewBox="0 0 20 32" fill="none" stroke="#222" stroke-width="2.5"><path d="M17 2L3 16l14 14"/></svg>
<div class="cat" style="left:75px"><div class="ph" role="img" aria-label="Silver pendant necklace with a round diamond cluster" style="background:linear-gradient(180deg,#f4ece4,#c9c9cc)"></div><h3>Pendant Necklaces</h3><span>Shop Now</span></div>
<div class="cat" style="left:436px"><div class="ph" role="img" aria-label="Long multicolour bead necklace" style="background:linear-gradient(180deg,#f4ece4,#7c9b8f)"></div><h3>Bead Necklaces</h3><span>Shop Now</span></div>
<div class="cat" style="left:798px"><div class="ph" role="img" aria-label="Pair of gold hoop earrings" style="background:linear-gradient(180deg,#f4ece4,#d7ad6a)"></div><h3>Earrings</h3><span>Shop Now</span></div>
<svg class="arrow" style="left:1140px;top:1028px" width="20" height="32" viewBox="0 0 20 32" fill="none" stroke="#222" stroke-width="2.5"><path d="M3 2l14 14L3 30"/></svg>

<section class="abs band"></section>
<h2 class="sec-title" style="top:1308px;color:var(--white)">Featured Products</h2>
<svg class="arrow" style="left:37px;top:1582px" width="16" height="28" viewBox="0 0 16 28" fill="none" stroke="#fff" stroke-width="2.5"><path d="M14 2L2 14l12 12"/></svg>
<svg class="arrow" style="left:1140px;top:1582px" width="16" height="28" viewBox="0 0 16 28" fill="none" stroke="#fff" stroke-width="2.5"><path d="M2 2l12 12L2 26"/></svg>

<div class="prod" style="left:75px"><div class="ph" role="img" aria-label="Rose gold bangle set with gemstones" style="background:linear-gradient(180deg,#fff,#e7c2a4)"></div><h4>Product Heading</h4><p>Sed ut perspiciatis unde nis iste natus</p><div class="price"><i><svg width="16" height="14" viewBox="0 0 20 18" fill="none" stroke="#b38a2c" stroke-width="2.4"><path d="M1 7h18l-2 10H3z M6 7l4-6 4 6"/></svg></i>$12.99</div></div>
<div class="prod" style="left:346px"><div class="ph" role="img" aria-label="Bracelet of orange, green and brown stone beads" style="background:linear-gradient(180deg,#fff,#b0703e 55%,#fff)"></div><h4>Product Heading</h4><p>Sed ut perspiciatis unde nis iste natus</p><div class="price"><i><svg width="16" height="14" viewBox="0 0 20 18" fill="none" stroke="#b38a2c" stroke-width="2.4"><path d="M1 7h18l-2 10H3z M6 7l4-6 4 6"/></svg></i>$12.99</div></div>
<div class="prod" style="left:615px"><div class="ph" role="img" aria-label="Rose gold hoop earrings" style="background:linear-gradient(180deg,#fff,#e3b690 50%,#fff)"></div><h4>Product Heading</h4><p>Sed ut perspiciatis unde nis iste natus</p><div class="price"><i><svg width="16" height="14" viewBox="0 0 20 18" fill="none" stroke="#b38a2c" stroke-width="2.4"><path d="M1 7h18l-2 10H3z M6 7l4-6 4 6"/></svg></i>$12.99</div></div>
<div class="prod" style="left:885px"><div class="ph" role="img" aria-label="Teardrop diamond drop earrings in gold" style="background:linear-gradient(180deg,#fff,#dcc3a5 50%,#fff)"></div><h4>Product Heading</h4><p>Sed ut perspiciatis unde nis iste natus</p><div class="price"><i><svg width="16" height="14" viewBox="0 0 20 18" fill="none" stroke="#b38a2c" stroke-width="2.4"><path d="M1 7h18l-2 10H3z M6 7l4-6 4 6"/></svg></i>$12.99</div></div>

<div class="btn" style="left:465px;top:1855px;width:270px;height:60px">View All Products</div>

<div class="promo" role="img" aria-label="Dark jade square pendant on a braided cord" style="left:75px;background:radial-gradient(ellipse at 50% 60%,#3f4538,#1f211e)">
  <div class="abs" style="left:0;top:170px;width:512px;font-size:48px;font-weight:700">New Arrivals</div>
  <div class="btn" style="left:156px;top:252px;width:200px;height:52px">Shop Now</div>
</div>
<div class="promo" role="img" aria-label="Diamond tennis bracelet on a velvet display" style="left:615px;background:radial-gradient(ellipse at 50% 50%,#6b5a40,#221d17)">
  <div class="abs" style="left:0;top:110px;width:512px;font-size:36px;font-weight:700">Upto</div>
  <div class="abs" style="left:0;top:142px;width:512px;font-size:88px;font-weight:800;line-height:100px">20% OFF</div>
  <div class="abs" style="left:0;top:242px;width:512px;font-size:36px;font-weight:700">Bracelets</div>
  <div class="btn" style="left:156px;top:310px;width:200px;height:52px">Shop Now</div>
</div>

<div class="abs about-img" role="img" aria-label="City skyline at dusk above a stone arch bridge over a river"></div>
<section class="abs about">
  <h2>About de Lorvanche<br>Jewelry &amp; Co</h2>
  <p>Sed ut perspiciatis unde omnis iste natus error sit voluptatem accusantium doloremque laudantium, totam rem aperiam, eaque ipsa quae ab illo inventore veritatis et quasi architecto beatae vitae dicta sunt explicabo. Nemo enim ipsam voluptatem quia voluptas sit aspernatur aut odit aut fugit, sed quia consequuntur magni dolores eos qui ratione voluptatem sequi nesciunt.</p>
  <div class="btn" style="left:28px;top:420px;width:168px;height:60px">Read More</div>
</section>

<h2 class="abs" style="left:72px;top:3195px;font-size:44px;font-weight:700">Latest Blog</h2>
<svg class="arrow" style="left:360px;top:3212px" width="18" height="30" viewBox="0 0 18 30" fill="none" stroke="#222" stroke-width="2.5"><path d="M15 2L3 15l12 13"/></svg>
<svg class="arrow" style="left:418px;top:3212px" width="18" height="30" viewBox="0 0 18 30" fill="none" stroke="#b38a2c" stroke-width="2.5"><path d="M3 2l12 13L3 28"/></svg>

<article class="blog" style="left:73px"><div class="ph" role="img" aria-label="Black triangular pendant on a dark stone surface" style="background:linear-gradient(160deg,#5d7283,#1d2a33)"></div><p>Nemo enim ipsam voluptatem quia voluptas sit aspernatur</p><time>June 15, 2024</time></article>
<article class="blog" style="left:436px"><div class="ph" role="img" aria-label="Gold pendants displayed on marble blocks" style="background:linear-gradient(160deg,#4a4a4a,#b9b3aa,#2a2a2a)"></div><p>Nemo enim ipsam voluptatem quia voluptas sit aspernatur</p><time>June 15, 2024</time></article>
<article class="blog" style="left:797px"><div class="ph" role="img" aria-label="Gold chain necklace with a small stone worn at the collarbone" style="background:linear-gradient(160deg,#b8806a,#6b3e30)"></div><p>Nemo enim ipsam voluptatem quia voluptas sit aspernatur</p><time>June 15, 2024</time></article>

<div class="btn" style="left:465px;top:3659px;width:270px;height:60px">Read All Posts</div>

<section class="abs email">
  <h2>Join Email Listing</h2>
  <p>Nemo enim ipsam voluptatem quia voluptas sit aspernatur</p>
  <div class="field">Enter Email Address</div>
  <svg class="abs" style="left:1086px;top:86px" width="18" height="18" viewBox="0 0 18 18" fill="none" stroke="#b38a2c" stroke-width="1.8"><path d="M1 8l16-7-6 16-2-7z M9 10l8-9"/></svg>
</section>

<div class="abs foot-logo">
  <div style="width:70px;height:70px;border:4px solid var(--gold);margin:0 auto 20px"></div>
  <div style="font-size:30px;font-weight:500;color:var(--charcoal);letter-spacing:1px">DE LORVANCHE</div>
  <div style="font-size:14px;color:var(--gold);letter-spacing:4px;margin-top:4px">JEWELRY &amp; CO.</div>
</div>

<div class="foot-col" style="left:370px"><h5>Navigations</h5><ul><li>Home</li><li>About Us</li><li>Products</li><li>Shop</li><li>Reviews</li><li>Contact</li></ul></div>
<div class="foot-col" style="left:614px"><h5>My Account</h5><ul><li>Excepteur sint occaecat</li><li>Cupidatat</li><li>Proidentsuntulpa</li><li>Qui officia deserunt</li><li>Mollit anim</li></ul></div>
<div class="foot-col contact" style="left:884px"><h5>Contact Us</h5><ul>
  <li><svg width="16" height="16" viewBox="0 0 16 16" fill="#b38a2c" style="margin-top:5px;flex:none"><path d="M8 0a5.5 5.5 0 015.5 5.5C13.5 10 8 16 8 16S2.5 10 2.5 5.5A5.5 5.5 0 018 0z"/></svg>27 Birchwood Lane, Alder Falls,<br>MN 55803</li>
  <li><svg width="16" height="16" viewBox="0 0 16 16" fill="#b38a2c" style="margin-top:5px;flex:none"><path d="M3 1l3 3-2 2c1 2 3 4 5 5l2-2 3 3-2 3C6 15 1 10 0 4z"/></svg>+1 218-555-0147</li>
  <li><svg width="16" height="12" viewBox="0 0 16 12" fill="#b38a2c" style="margin-top:7px;flex:none"><path d="M0 0h16v12H0z"/><path d="M0 0l8 6 8-6" stroke="#fff" fill="none"/></svg>hello@delorvanche-example.com</li>
</ul>
  <div style="display:flex;gap:16px;margin-top:14px">
    <span style="width:22px;height:22px;border-radius:50%;background:var(--gold)"></span>
    <span style="width:22px;height:22px;border-radius:50%;background:var(--gold)"></span>
    <span style="width:22px;height:22px;border-radius:50%;background:var(--gold)"></span>
    <span style="width:22px;height:22px;border-radius:50%;background:var(--gold)"></span>
    <span style="width:22px;height:22px;border-radius:50%;background:var(--gold)"></span>
  </div>
</div>

<footer class="abs copy">
  <div class="abs" style="left:73px;top:30px;font-size:13px;color:var(--muted)">© Copyright 2024. All Rights Reserved.</div>
  <div class="abs" style="left:955px;top:24px;display:flex;gap:20px">
    <span style="width:28px;height:20px;border-radius:3px;background:#888"></span>
    <span style="width:28px;height:20px;border-radius:3px;background:#888"></span>
    <span style="width:28px;height:20px;border-radius:3px;background:#888"></span>
    <span style="width:28px;height:20px;border-radius:3px;background:#888"></span>
  </div>
</footer>

</body>
</html>
```